Packaging and logo design for washcloths

We are a company manufacturing towels and washcloths for babies.We are planning to get into e-commerce business with washcloths for babies made out of 100% Rayon made from Bamboo.We would like to see a logo design that symbolizes the perfection of the nature and a packaging design that gives mothers the feeling of cleanliness,pureness, softness and eco-friendliness. The packaging will include 6 items, each washcloth is 10x10 inches. The details will be discussed with the designer.

Looking for a clean and neat design that will attract the buyers which will also emphasize the fact that it is made out of highest quality rayon from bamboo that don’t irritate sensitive and delicate skin. I am planning to outsource more work (website,flyers, pictures and social media related stuff) to the designers who does the best job for this packaging project .

Target Market(s)

E-commerce customers, mothers,

Colors

Designer to choose colors to be used in the design.

Requirements
Must have
• clean and stylish look that should emphasize the fact that the product is 100% organic bamboo, eco-friendly,premium ultra soft, perfect for delicate and sensitive skin and 100% natural.Kraft paper packaging might be more suitable for an eco-friendly, bamboo based product.
Nice to have
• Packaging dimensions of our first competitors is 8.3 x 5.6 x 1.4 inches and the second one is 8.2 x 5.8 x 1.5 inches therefore; the final product should be designed according to these dimensions keeping in mind that each box will have 6 towels in it.

```html
<!DOCTYPE html>
<html lang="en">
<head>
<meta charset="utf-8">
<title>Leafnest Pure Bamboo Washcloth Box – Front Panel</title>
<link rel="stylesheet" href="https://fonts.googleapis.com/css2?family=Bungee&family=Roboto:ital,wght@0,400;0,500;0,700;0,900;1,700&display=swap">
<style>
  :root {
    --stage: #e4e5e6;
    --paper: #ffffff;
    --leaf: #7cc242;
    --leaf-deep: #5aa82a;
    --leaf-pale: #c9e4a6;
    --sky: #149ddd;
    --sky-deep: #0b7fc4;
    --ink-grey: #6d6e70;
    --illustration-a: #d8c8e6;
    --illustration-b: #f2cfd2;
    --illustration-c: #cfe0f0;
  }
  * { box-sizing: border-box; margin: 0; padding: 0; }
  html, body {
    width: 1200px; height: 582px; overflow: hidden;
    background: var(--stage);
  }
  .front-panel {
    position: absolute; left: 193px; top: 6px;
    width: 813px; height: 570px;
    background: var(--paper);
    overflow: hidden;
    font-family: "Roboto", Arial, sans-serif;
  }
  .panel-waves { position: absolute; inset: 0; width: 813px; height: 570px; }
  .product-illustration {
    position: absolute; left: 48px; top: 36px;
    width: 320px; height: 450px;
    border-radius: 18px;
    background: linear-gradient(180deg, var(--illustration-a) 0%, var(--illustration-b) 40%, var(--illustration-c) 65%, var(--illustration-b) 100%);
  }
  .brand-name {
    position: absolute; left: 414px; width: 394px; top: 118px;
    text-align: center;
    font-weight: 900; font-size: 44px; letter-spacing: 1px;
    color: var(--leaf-deep);
  }
  .brand-name .brand-dot {
    display: inline-block; width: 16px; height: 16px; border-radius: 50%;
    background: var(--leaf-deep); margin-right: 10px; vertical-align: middle;
  }
  .product-title {
    position: absolute; left: 414px; width: 394px; top: 206px;
    text-align: center; white-space: nowrap;
    font-family: "Bungee", "Roboto", sans-serif; font-weight: 400;
    font-size: 42px; line-height: 46px; letter-spacing: 0;
    color: var(--leaf);
    transform: scaleY(1.2); transform-origin: center top;
  }
  .material-bar {
    position: absolute; left: 414px; width: 394px; top: 268px; height: 40px;
    background: var(--sky);
    color: #fff; text-align: center; white-space: nowrap;
    font-size: 27px; line-height: 40px; font-weight: 400; letter-spacing: 0.5px;
  }
  .benefit-row {
    position: absolute; left: 458px; top: 330px;
    display: flex; list-style: none;
  }
  .benefit {
    width: 88px; text-align: center;
    font-size: 11.5px; font-weight: 500; color: var(--ink-grey);
    padding-top: 4px;
  }
  .benefit + .benefit { border-left: 1px solid #b7b8ba; }
  .benefit svg { display: block; margin: 0 auto 10px; width: 26px; height: 26px; }
  .website {
    position: absolute; left: 414px; width: 340px; top: 398px;
    text-align: center;
    font-size: 13.5px; font-weight: 700; letter-spacing: 2.4px;
    color: var(--sky);
  }
  .website-rule {
    position: absolute; left: 462px; width: 250px; top: 420px;
    border-top: 1px solid var(--leaf);
  }
  .count-badge { position: absolute; left: 661px; top: 424px; width: 128px; height: 128px; }
  .care-note {
    position: absolute; left: 26px; top: 520px;
    font-size: 10.5px; line-height: 15px; color: #fff;
  }
</style>
</head>
<body>
<main class="front-panel">

  <svg class="panel-waves" viewBox="0 0 813 570" aria-hidden="true">
    <path d="M250,0 C420,52 620,46 813,14 L813,0 Z" fill="var(--leaf-pale)"/>
    <path d="M300,0 C470,40 650,36 813,8" fill="none" stroke="var(--leaf)" stroke-width="2"/>
    <path d="M0,462 C260,432 520,470 813,360 L813,570 L0,570 Z" fill="var(--leaf)"/>
    <path d="M0,486 C260,458 520,500 813,410 L813,570 L0,570 Z" fill="#fff"/>
    <path d="M0,494 C260,470 520,516 813,430 L813,570 L0,570 Z" fill="var(--sky)"/>
    <path d="M0,520 C280,500 520,540 813,470" fill="none" stroke="var(--sky-deep)" stroke-width="2" opacity="0.6"/>
    <path d="M420,570 C600,548 720,520 813,478 L813,570 Z" fill="var(--leaf)"/>
  </svg>

  <div class="product-illustration" role="img"
       aria-label="Illustration of two green bamboo stalks with leaves, whose windows show a stack of folded pastel washcloths in lilac, pink and pale blue"></div>

  <div class="brand-name"><span class="brand-dot"></span>Leafnest</div>

  <h1 class="product-title">PURE BAMBOO</h1>
  <div class="material-bar">100% RAYON WASHCLOTH</div>

  <ul class="benefit-row">
    <li class="benefit">
      <svg viewBox="0 0 26 26" aria-hidden="true">
        <rect x="3" y="9" width="14" height="7" rx="3.5" transform="rotate(-35 10 12.5)" fill="var(--ink-grey)"/>
        <rect x="10" y="12" width="14" height="7" rx="3.5" transform="rotate(-35 17 15.5)" fill="#9a9b9d"/>
      </svg>
      Hypoallergenic
    </li>
    <li class="benefit">
      <svg viewBox="0 0 26 26" aria-hidden="true">
        <g stroke="var(--ink-grey)" stroke-width="2" stroke-linecap="round">
          <line x1="13" y1="2" x2="13" y2="24"/><line x1="2" y1="13" x2="24" y2="13"/>
          <line x1="5" y1="5" x2="21" y2="21"/><line x1="21" y1="5" x2="5" y2="21"/>
        </g>
        <circle cx="13" cy="13" r="7" fill="var(--ink-grey)"/>
      </svg>
      Antibacterial
    </li>
    <li class="benefit">
      <svg viewBox="0 0 26 26" aria-hidden="true">
        <path d="M4,22 C4,10 12,4 23,4 C23,15 16,22 4,22 Z" fill="var(--ink-grey)"/>
        <path d="M4,22 L16,11" stroke="#fff" stroke-width="1.5"/>
      </svg>
      Antibacterial
    </li>
  </ul>

  <div class="website">www.leafnestbaby.com</div>
  <div class="website-rule"></div>

  <svg class="count-badge" viewBox="-64 -64 128 128" aria-label="6 premium washcloth, 10x10 inches">
    <g transform="rotate(-14)">
      <polygon fill="#fff" points="62,0 54.1,14.5 53.7,31 39.6,39.6 31,53.7 14.5,54.1 0,62 -14.5,54.1 -31,53.7 -39.6,39.6 -53.7,31 -54.1,14.5 -62,0 -54.1,-14.5 -53.7,-31 -39.6,-39.6 -31,-53.7 -14.5,-54.1 0,-62 14.5,-54.1 31,-53.7 39.6,-39.6 53.7,-31 54.1,-14.5"/>
      <circle r="52" fill="var(--leaf)"/>
      <circle r="46" fill="none" stroke="#fff" stroke-width="1.5"/>
      <text x="-4" y="-8" text-anchor="end" font-family="Roboto, sans-serif" font-weight="900" font-size="40" fill="#fff">6</text>
      <text x="0" y="-18" font-family="Roboto, sans-serif" font-style="italic" font-weight="700" font-size="11" fill="#fff">premium</text>
      <text x="0" y="14" text-anchor="middle" font-family="Roboto, sans-serif" font-style="italic" font-weight="700" font-size="19" fill="#fff">washcloth</text>
      <text x="0" y="32" text-anchor="middle" font-family="Roboto, sans-serif" font-weight="500" font-size="8.5" fill="#fff">10X10 INCHES</text>
    </g>
  </svg>

  <p class="care-note">The hypoallergenic, soft, anti-bacterial fibres mean that even sensitive skin or eczema<br>will not be irritated and your baby enjoys bathtime without getting hurt.</p>

</main>
</body>
</html>
```